Jewellery retailer needs a flyer design please

We need a flyer to represent our business.

Our company provides The lowest priced diamonds in Australia.
We are wholesales who sell direct to the public
We GENUINELY are 50-70% cheaper than other retail stores.

We guarantee the lowest prices, even in the unlikely event a customer finds a cheaper price than ours, we will beat it too.

Well tell our customers if youre not buying from us then you're paying too much.

Please include website www.amberloomstore.com.au
and facebook page www.facebook.com/mosslightcove.

We have location in Harbourgate Parramatta, and Harbourgate Liverpool, NSW.

Im sorry, this is the first time ive done this, so i hope ive given the information you need.

Target Market(s)

People wanting to buy engagement rings are our biggest customers.

Industry/Entity Type

Retail

Colors
276db0
3276b5
86acd3
cedeed

Requirements
Must have
• Simple, to the point! We need people to know that we have the lowest prices without compromising on quality
Nice to have
• I am very very open to anything. I do not have any particular expectations

```html
<!DOCTYPE html>
<html lang="en">
<head>
<meta charset="utf-8">
<title>Amber Loom – Wholesale Diamonds Flyer</title>
<link rel="stylesheet" href="https://fonts.googleapis.com/css2?family=Alegreya+Sans:wght@400;500;700&family=Sofia&display=swap">
<style>
  :root {
    --brand-deep: #276db0;
    --brand-mid: #3276b5;
    --brand-soft: #86acd3;
    --brand-pale: #cedeed;
    --frame: #d6e4f2;
    --ink: #1f2430;
    --logo-ink: #3b4766;
    --rule: #9fbde0;
    --stage: #f2f2f2;
    --paper: #ffffff;
    --silver: #b9c0ca;
    --silver-light: #e4e7ec;
  }
  * { margin: 0; padding: 0; box-sizing: border-box; }
  html, body { width: 1200px; height: 1000px; overflow: hidden; background: var(--stage); }
  .flyer {
    position: absolute; left: 314px; top: 93px; width: 574px; height: 815px;
    background: linear-gradient(180deg, var(--brand-deep) 0%, #4f86c2 18%, var(--brand-soft) 34%, #a9c5e3 46%, var(--brand-pale) 60%, #eef4fa 70%, var(--paper) 76%);
    font-family: "Alegreya Sans", sans-serif; color: var(--ink); text-align: center;
    font-variant-numeric: lining-nums;
  }
  .headline {
    position: absolute; left: 0; top: 48px; width: 100%;
    font-family: "Sofia", cursive; font-size: 35px; line-height: 48px; font-weight: 400;
    color: var(--paper); text-shadow: 0 2px 4px rgba(0,0,0,.25);
  }
  .offer {
    position: absolute; left: 0; top: 146px; width: 100%;
    font-size: 50px; line-height: 60px; font-weight: 700; color: var(--paper);
    text-shadow: 0 2px 4px rgba(0,0,0,.25);
  }
  .photo {
    position: absolute; border: 4px solid var(--frame); background: var(--paper);
  }
  .photo span { display: block; width: 100%; height: 100%;
    background: radial-gradient(ellipse 55% 30% at 50% 55%, var(--silver) 0%, var(--silver-light) 55%, var(--paper) 100%); }
  .photo--a { left: 24px; top: 230px; width: 117px; height: 118px; }
  .photo--b { left: 24px; top: 357px; width: 117px; height: 118px; }
  .photo--feature { left: 150px; top: 230px; width: 273px; height: 245px; }
  .photo--feature span { background: radial-gradient(ellipse 45% 35% at 50% 50%, var(--silver) 0%, var(--silver-light) 55%, var(--paper) 100%); }
  .photo--c { left: 432px; top: 230px; width: 117px; height: 118px; }
  .photo--d { left: 432px; top: 357px; width: 117px; height: 118px; }
  .pitch {
    position: absolute; left: 0; top: 503px; width: 100%;
    font-size: 15.5px; line-height: 19.5px;
  }
  .pitch .invite { font-size: 17.5px; margin-top: 3px; }
  .brand {
    position: absolute; left: 0; top: 648px; width: 100%;
    display: flex; align-items: center; justify-content: center; gap: 12px;
    font-size: 40px; line-height: 48px; font-weight: 500; color: var(--logo-ink); letter-spacing: 1px;
  }
  .brand-dot { width: 14px; height: 14px; border-radius: 50%; background: var(--brand-soft); }
  .address { position: absolute; left: 0; top: 723px; width: 100%; font-size: 15.5px; line-height: 20px; }
  .rule { position: absolute; left: 82px; top: 756px; width: 410px; height: 1px; background: var(--rule); }
  .links { position: absolute; left: 0; top: 767px; width: 100%; font-size: 13.5px; line-height: 18px; }
  .links .sep { margin: 0 7px; }
</style>
</head>
<body>
<main class="flyer">
  <h1 class="headline">Wholesale diamonds with<br>Sparkling discounts</h1>
  <p class="offer">Get 50-70% off!</p>

  <div class="photo photo--a"><span role="img" aria-label="Emerald-cut diamond engagement ring on white"></span></div>
  <div class="photo photo--b"><span role="img" aria-label="Halo diamond engagement ring on white"></span></div>
  <div class="photo photo--feature"><span role="img" aria-label="Princess-cut diamond ring with matching channel-set band"></span></div>
  <div class="photo photo--c"><span role="img" aria-label="Marquise solitaire diamond ring on white"></span></div>
  <div class="photo photo--d"><span role="img" aria-label="Three-stone emerald-cut diamond ring on white"></span></div>

  <div class="pitch">
    <p>We offer the finest quality diamonds in various cuts, colours and designs<br>
    in unbeatable prices, because we want to show that you are special.<br>
    We challenge you to find a price that is cheaper than ours.</p>
    <p class="invite">So come over, Indulge.</p>
  </div>

  <p class="brand"><span class="brand-dot"></span>Amber Loom</p>
  <p class="address">Harbourgate Parramatta and Harbourgate Liverpool, NSW.</p>
  <div class="rule"></div>
  <p class="links">www.amberloomstore.com.au<span class="sep">|</span>www.facebook.com/mosslightcove</p>
</main>
</body>
</html>
```